Lantern Path Collective

Re-design our website www.lanternpathco.org
We are a non profit catering for adults, elderly, veterans and youth in impoverished neighborhoods to improve their digital access and help them improve their lives and better our community.

I need the text on home page to stay. Its the first message vsitors shd read when they arrive on our page.

Number of Pages Required

4 page

Font styles to use
Other font styles liked:
• color and font shd be like the image attched below.

```html
<!DOCTYPE html>
<html lang="en">
<head>
<meta charset="utf-8">
<title>Lantern Path Collective</title>
<link href="https://fonts.googleapis.com/css2?family=Poppins:wght@400;500;600;700&family=Arimo:wght@400&display=swap" rel="stylesheet">
<style>
:root{
  --blue-deep:#0a6fe0;
  --blue-bright:#0ab4f2;
  --sky:#93c6de;
  --sky-line:#9ccbe0;
  --green:#c5df9a;
  --orange:#fbc89a;
  --ink:#222;
  --grey-text:#8a8a8a;
  --card-grey:#9a9a9a;
  --footer:#3d3d3d;
  --donate-blue:#1a73e8;
  --white:#fff;
}
*{margin:0;padding:0;box-sizing:border-box}
html,body{width:1200px;height:2572px;overflow:hidden;background:var(--white)}
body{position:relative;font-family:"Arimo",Arial,sans-serif;color:var(--ink)}
.abs{position:absolute}
.poppins{font-family:"Poppins",Arial,sans-serif}

/* hero */
.hero{left:0;top:0;width:1200px;height:576px;background:linear-gradient(180deg,var(--blue-deep) 0%,#0b8ae8 45%,var(--blue-bright) 100%);overflow:hidden}
.hero-curve{left:0;top:0}
.brand{display:flex;align-items:center;gap:8px;color:var(--white);font-family:"Poppins",sans-serif;font-weight:700;font-size:17px;line-height:20px}
.brand-dot{width:18px;height:18px;border-radius:50%;background:var(--white);flex:none}
.nav{left:364px;top:51px;display:flex;gap:0;font-family:"Poppins",sans-serif;font-weight:600;font-size:13px;color:var(--white)}
.nav span{margin-right:21px;display:flex;align-items:center;gap:5px}
.caret{width:0;height:0;border-left:4px solid transparent;border-right:4px solid transparent;border-top:5px solid var(--white)}
.btn-donate-top{left:997px;top:45px;width:86px;height:31px;background:var(--white);border-radius:5px;color:#111;font-family:"Poppins",sans-serif;font-weight:600;font-size:13px;display:flex;align-items:center;justify-content:center}
.hero-title{left:119px;top:222px;font-family:"Poppins",sans-serif;font-weight:700;font-size:43px;line-height:50px;color:var(--white)}
.hero-sub{left:119px;top:334px;width:460px;font-size:16px;line-height:21px;color:var(--white)}
.hero-photo{left:632px;top:240px;width:530px;height:336px;border-radius:200px 200px 0 40px;background:linear-gradient(135deg,#e9b48c 0%,#f3a25a 45%,#f0f0f2 100%)}

/* about */
.about-photo{left:51px;top:765px;width:514px;height:340px;border-radius:50%;background:linear-gradient(120deg,#c99a78 0%,#3aa7d8 50%,#6b8aa0 100%)}
.about-title{left:630px;top:738px;font-family:"Poppins",sans-serif;font-weight:700;font-size:30px;color:var(--orange)}
.about-text{left:630px;top:802px;width:445px;font-size:14px;line-height:25.8px;color:var(--grey-text)}
.btn-know{left:630px;top:980px;width:155px;height:45px;background:var(--green);font-family:"Poppins",sans-serif;font-weight:600;font-size:13px;color:#333;display:flex;align-items:center;justify-content:center;letter-spacing:.3px}

/* mission box */
.mission-frame{left:120px;top:1160px;width:962px;height:461px;border:2px solid var(--sky-line);border-radius:42px}
.mission{left:131px;top:1172px;width:941px;height:438px;background:var(--sky);border-radius:36px}
.mission-text{left:217px;top:1244px;width:775px;font-size:14px;line-height:20.6px;color:var(--ink)}
.mission-text p{margin-bottom:20.6px}
.mission-text .accent{font-family:"Poppins",sans-serif;font-weight:600;color:var(--white);font-size:14px;line-height:20.6px}

/* explore */
.explore-title{left:200px;top:1703px;width:800px;text-align:center;font-family:"Poppins",sans-serif;font-weight:700;font-size:31px;line-height:37px;color:var(--green)}
.explore-text{left:235px;top:1826px;width:730px;text-align:center;font-size:14px;line-height:20.6px;color:var(--grey-text)}
.card{top:1940px;width:225px;height:228px;border:2px solid;display:flex;flex-direction:column;align-items:center}
.card svg{margin-top:38px}
.card-label{position:absolute;top:170px;width:100%;text-align:center;font-family:"Poppins",sans-serif;font-weight:600;font-size:13px;color:#222}
.card-blue{left:120px;border-color:var(--sky)}
.card-green{left:366px;border-color:var(--green)}
.card-orange{left:612px;border-color:var(--orange)}
.card-grey{left:858px;border-color:var(--card-grey)}

/* footer */
.footer{left:0;top:2243px;width:1200px;height:329px;background:var(--footer);color:var(--white);font-family:"Poppins",sans-serif}
.footer .brand{font-size:16px}
.f-brand{left:120px;top:60px;width:170px}
.btn-donate-foot{left:120px;top:185px;width:129px;height:33px;background:var(--donate-blue);border-radius:5px;font-weight:600;font-size:13px;display:flex;align-items:center;justify-content:center}
.f-col{top:57px;font-size:14px;line-height:26px;font-weight:500}
.f-col h4{font-weight:600;font-size:15px;line-height:26px;margin-bottom:26px}
.f-rule{left:113px;top:267px;width:987px;height:1px;background:#cfcfcf}
.f-legal{left:119px;top:295px;font-size:13px;font-weight:600;display:flex;gap:28px}
.socials{left:874px;top:287px;display:flex;gap:22px}
.socials span{width:34px;height:34px;border-radius:50%;background:var(--white)}
</style>
</head>
<body>

<header class="abs hero">
  <svg class="abs hero-curve" width="1200" height="576" viewBox="0 0 1200 576"><path d="M0 452 Q600 690 1200 452 L1200 576 L0 576 Z" fill="#fff"/></svg>
  <div class="abs hero-photo" role="img" aria-label="Photo of three smiling children looking at a laptop"></div>
  <div class="abs brand" style="left:120px;top:38px;width:170px"><span class="brand-dot"></span>Lantern Path Collective</div>
  <nav class="abs nav">
    <span>HOME</span>
    <span>GET CONNECTED <i class="caret"></i></span>
    <span style="margin-right:9px">E-WASTE SERVICES <i class="caret"></i></span>
    <span>OUR IMPACT</span>
    <span>ABOUT <i class="caret"></i></span>
    <span>CONTACT</span>
  </nav>
  <div class="abs btn-donate-top">DONATE</div>
  <h1 class="abs hero-title">Creating a Social<br>Impact with e-Waste</h1>
  <p class="abs hero-sub">By transforming Unwanted Technology into Opportunities for People In-Need.</p>
</header>

<section>
  <div class="abs about-photo" role="img" aria-label="Photo of smiling students seated at classroom computers"></div>
  <h2 class="abs about-title">ABOUT US</h2>
  <p class="abs about-text">Lantern Path Collective is a nonprofit and social enterprise that creates equitable access to opportunity by providing devices, internet access, digital skills training, and tech support for low-income families, the homeless, and Veterans in our communities while at the same time, empowering businesses and organizations to do good by diverting technology from landfills to protect our planet.</p>
  <div class="abs btn-know">KNOW MORE</div>
</section>

<section>
  <div class="abs mission-frame"></div>
  <div class="abs mission"></div>
  <div class="abs mission-text">
    <p>Being digitally literate is no longer a luxury, it is a must-have skill for everyone to manage information, communicate, manage money, and access support plus other government services. It has become an essential tool for modern-day citizenship and participation; no one can afford to be left behind.</p>
    <p>Unfortunately, nearly 100 million Americans lack access to a personal computer, internet connection, or both. This lack of access to digital technology creates a significant gap between the opportunities unconnected people can access and the ones digitally native households can. This gap in opportunities is known as the digital divide, and it’s our mission by joining hands with many other organizations that are tirelessly trying to shrink it because we believe that equitable access to information and technology empowers people to achieve their fullest potential.</p>
    <p class="accent">At the same time Electronic waste, or e-waste, refers to electronic products and components that are unwanted, unusable, or nearing the end of their useful life. While e-waste only makes up 2% of the mass in landfills, it accounts for 70% of toxic waste. Unfortunately, recycling is no longer a sufficient method for disposing of waste sustainably; given the scale of the climate crisis, reuse is now a prerequisite for protecting our planet.</p>
  </div>
</section>

<section>
  <h2 class="abs explore-title">EXPLORE OPPORTUNITIES ONLINE WITH LOW-COST TECHNOLOGY, INTERNET, TRAINING AND SUPPORT.</h2>
  <p class="abs explore-text">In order to comprehensively shrink the digital divide, we offer you access to low-cost computers, low-cost internet, free digital literacy training and tech support. Click the boxes below to explore how we can help you and members of your community unlock their full potential through digital technology.</p>

  <div class="abs card card-blue">
    <svg width="130" height="100" viewBox="0 0 130 100" fill="none" stroke="#93c6de" stroke-width="4"><rect x="15" y="20" width="100" height="64"/><rect x="24" y="28" width="82" height="48"/><path d="M3 96 L12 84 H118 L127 96 Z"/><path d="M48 60 L64 44 M62 62 L84 42" stroke-width="3"/></svg>
    <div class="card-label">AFFORTABLE TECHNOLOGY</div>
  </div>
  <div class="abs card card-green">
    <svg width="130" height="100" viewBox="0 0 130 100" fill="none" stroke="#c5df9a" stroke-width="10" stroke-linecap="round"><path d="M10 40 Q65 -5 120 40"/><path d="M30 58 Q65 28 100 58"/><path d="M50 74 Q65 64 80 74"/><circle cx="65" cy="92" r="5" fill="#c5df9a" stroke="none"/></svg>
    <div class="card-label">INTERNET ACCESS</div>
  </div>
  <div class="abs card card-orange">
    <svg width="130" height="110" viewBox="0 0 130 110" fill="none" stroke="#fbc89a" stroke-width="4" stroke-linecap="round" style="margin-top:30px"><path d="M65 4 V16 M24 20 L32 28 M106 20 L98 28 M10 52 H22 M108 52 H120 M24 82 L32 76 M106 82 L98 76"/><path d="M65 28 C45 28 36 44 40 58 C43 68 52 72 52 82 H78 C78 72 87 68 90 58 C94 44 85 28 65 28 Z"/><path d="M54 88 H76 M56 96 H74"/></svg>
    <div class="card-label">DIGITAL LITERACY TRAINING</div>
  </div>
  <div class="abs card card-grey">
    <svg width="130" height="110" viewBox="0 0 130 110" fill="none" stroke="#9a9a9a" stroke-width="3.5" stroke-linecap="round" style="margin-top:42px"><path d="M24 60 V46 C24 20 44 6 65 6 C86 6 106 20 106 46 V60"/><rect x="18" y="52" width="14" height="26" rx="6"/><rect x="98" y="52" width="14" height="26" rx="6"/><path d="M105 78 C105 94 90 104 74 104"/><rect x="60" y="100" width="14" height="8" rx="3"/></svg>
    <div class="card-label">TECH SUPPORT</div>
  </div>
</section>

<footer class="abs footer">
  <div class="abs brand f-brand"><span class="brand-dot"></span>Lantern Path Collective</div>
  <div class="abs btn-donate-foot">DONATE</div>

  <div class="abs f-col" style="left:357px">
    <h4>GET CONNECTED</h4>
    Get Technology<br>Low-Cost Internet<br>Digital Training<br>Tech Support<br>FOr Organizations
  </div>
  <div class="abs f-col" style="left:539px;width:160px">
    <h4 style="margin-bottom:26px">REPOURPOSE YOUR TECH</h4>
    E-Waste Services<br>Data Destruction<br>Technology Drives
  </div>
  <div class="abs f-col" style="left:738px">
    <h4>ABOUT US</h4>
    Our Story<br>Our Impact
  </div>
  <div class="abs f-col" style="left:873px">
    <h4>CONTACT</h4>
    (555) 014-2270<br>info@lanternpathco.org<br>418 Harbor Lane,<br>Maple Springs, CA 90000
  </div>

  <div class="abs f-rule"></div>
  <div class="abs f-legal"><span>© 2023 BY LANTERN PATH COLLECTIVE. ALL RIGHTS RESERVED.</span><span>|</span><span>PRIVACY &amp; SECURITY POLICY</span></div>
  <div class="abs socials" aria-label="Social media links"><span></span><span></span><span></span><span></span></div>
</footer>

</body>
</html>
```